FotoVELTA buisnesscard

Hey :) I need a modern buisnesscard for my company FotoVELTA
It most have:
Dagligleder og Fotograf: Henrik Torvald Bjelland

Mob: +4791642058
Epost: post@fotovelta.no
Adresse: Bakkestien22, 6041 Nordvik

Facbook and instagram logo with text FotoVELTA

FotoVELTA logo

It Company

```html
<!DOCTYPE html>
<html lang="no">
<head>
<meta charset="utf-8">
<title>FotoVELTA – visittkort</title>
<link rel="stylesheet" href="https://fonts.googleapis.com/css2?family=Ubuntu:wght@400;500;700&display=swap">
<style>
  :root {
    --stage: #d9dcdf;
    --card-black: #151515;
    --card-grey: #262626;
    --ink-white: #f4f4f4;
    --accent-cyan: #3fb6d9;
    --accent-pink: #f1a6c6;
    --font-main: "Ubuntu", sans-serif;
  }
  html, body {
    margin: 0;
    width: 1200px;
    height: 872px;
    overflow: hidden;
    background: var(--stage);
    font-family: var(--font-main);
  }
  .sheet {
    width: 1200px;
    height: 872px;
    display: flex;
    align-items: center;
    justify-content: center;
    gap: 40px;
  }
  .card {
    position: relative;
    width: 540px;
    height: 309px;
    border-radius: 4px;
    overflow: hidden;
    box-shadow: 0 8px 24px rgba(0,0,0,.25);
    color: var(--ink-white);
  }

  /* Front side */
  .card--front {
    background: linear-gradient(135deg, #1d1d1d 0%, var(--card-black) 60%, #0f0f0f 100%);
  }
  .brand-mark {
    position: absolute;
    top: 52px;
    left: 0;
    right: 0;
    text-align: center;
    font-weight: 700;
    font-size: 30px;
    letter-spacing: .5px;
    color: var(--ink-white);
  }
  .identity {
    position: absolute;
    top: 118px;
    left: 0;
    right: 0;
    text-align: center;
  }
  .identity__name {
    font-weight: 500;
    font-size: 24px;
    margin: 0;
  }
  .identity__role {
    font-size: 17px;
    letter-spacing: .6px;
    color: var(--accent-cyan);
    margin: 6px 0 0;
  }
  .contacts {
    position: absolute;
    left: 28px;
    bottom: 24px;
    list-style: none;
    margin: 0;
    padding: 0;
    font-size: 11.5px;
  }
  .contacts li {
    display: flex;
    align-items: center;
    gap: 8px;
    margin-top: 7px;
  }
  .contact-icon {
    width: 15px;
    height: 15px;
    flex: none;
  }
  .social {
    position: absolute;
    right: 30px;
    bottom: 24px;
    display: flex;
    align-items: center;
    gap: 8px;
    font-size: 13px;
  }
  .social__dot {
    width: 13px;
    height: 13px;
    border-radius: 50%;
    background: var(--accent-cyan);
  }

  /* Back side */
  .card--back {
    background:
      linear-gradient(118deg, transparent 0 22%, rgba(255,255,255,.05) 22% 30%, transparent 30%),
      linear-gradient(62deg, transparent 0 70%, rgba(255,255,255,.05) 70% 78%, transparent 78%),
      radial-gradient(ellipse at center, #1a1a1a 0%, var(--card-black) 55%, var(--card-grey) 100%);
    display: flex;
    align-items: center;
    justify-content: center;
  }
  .back-brand {
    font-weight: 700;
    font-size: 46px;
    color: var(--accent-cyan);
    letter-spacing: .5px;
  }
</style>
</head>
<body>
<main class="sheet">
  <section class="card card--front" aria-label="Visittkort forside">
    <div class="brand-mark">FotoVELTA</div>
    <div class="identity">
      <h1 class="identity__name">Henrik Torvald Bjelland</h1>
      <p class="identity__role">Dagligleder og Fotograf</p>
    </div>
    <ul class="contacts">
      <li>
        <svg class="contact-icon" viewBox="0 0 16 16" aria-hidden="true">
          <circle cx="8" cy="8" r="8" fill="var(--accent-cyan)"/>
          <path d="M5.2 4.2l1.5-.3.8 1.9-1 .8a6 6 0 0 0 2.9 2.9l.8-1 1.9.8-.3 1.5c-3.6.3-6.9-3-6.6-6.6z" fill="#151515"/>
        </svg>
        <span>+4791642058</span>
      </li>
      <li>
        <svg class="contact-icon" viewBox="0 0 16 16" aria-hidden="true">
          <circle cx="8" cy="8" r="8" fill="var(--accent-cyan)"/>
          <rect x="4" y="5" width="8" height="6" rx=".6" fill="#151515"/>
          <path d="M4.3 5.4L8 8.3l3.7-2.9" stroke="var(--accent-cyan)" stroke-width=".9" fill="none"/>
        </svg>
        <span>post@fotovelta.no</span>
      </li>
      <li>
        <svg class="contact-icon" viewBox="0 0 16 16" aria-hidden="true">
          <circle cx="8" cy="8" r="8" fill="var(--accent-cyan)"/>
          <path d="M8 3.5a3 3 0 0 0-3 3c0 2.2 3 6 3 6s3-3.8 3-6a3 3 0 0 0-3-3z" fill="#151515"/>
          <circle cx="8" cy="6.5" r="1.1" fill="var(--accent-cyan)"/>
        </svg>
        <span>Bakkestien22, 6041 Nordvik</span>
      </li>
    </ul>
    <div class="social">
      <span class="social__dot" aria-hidden="true"></span>
      <span>FotoVELTA</span>
    </div>
  </section>

  <section class="card card--back" aria-label="Visittkort bakside">
    <div class="back-brand">FotoVELTA</div>
  </section>
</main>
</body>
</html>
```